Harrowby Lending Hard Money Lender

We are looking for this flyer to be redesigned. We would like it to be even more simple than the attached design. No photos, no exclamation points, a 3-4 color palate maximum. We would do not want any graphics around the "Harrowby Lending" logo.

```html
<!DOCTYPE html>
<html lang="en">
<head>
<meta charset="utf-8">
<title>Harrowby Lending – Hard Money Loans</title>
<link rel="stylesheet" href="https://fonts.googleapis.com/css2?family=Montserrat:wght@800&family=Work+Sans:wght@500;600&family=Lato:wght@400&display=swap">
<style>
  :root {
    --navy: #0b2a6b;
    --blue: #1552b0;
    --blue-light: #2a6fd1;
    --ink: #2b3a8f;
    --text: #1f1f2a;
    --grey: #dfe2e8;
    --white: #ffffff;
  }
  html, body { margin: 0; padding: 0; overflow: hidden; background: var(--white); }
  .flyer {
    position: relative; width: 992px; height: 1200px; overflow: hidden;
    background: var(--white); font-family: "Work Sans", sans-serif;
  }
  .flyer-shapes { position: absolute; inset: 0; }
  .brand {
    position: absolute; left: 150px; top: 70px; margin: 0;
    color: var(--white); font-family: "Work Sans", sans-serif; font-weight: 500;
    font-size: 44px; letter-spacing: 3px; line-height: 1.1;
  }
  .headline {
    position: absolute; left: 48px; top: 478px; margin: 0;
    font-family: "Montserrat", sans-serif; font-weight: 800; font-size: 54px;
    color: var(--navy); letter-spacing: -0.5px;
  }
  .rate {
    position: absolute; left: 50px; top: 545px; margin: 0;
    font-family: "Work Sans", sans-serif; font-weight: 600; font-size: 21px; color: var(--ink);
  }
  .services { position: absolute; left: 0; top: 575px; width: 992px; height: 240px; }
  .service {
    position: absolute; top: 0; width: 290px; text-align: center;
  }
  .service svg { display: block; margin: 0 auto; }
  .service-label {
    margin: 16px 0 0; font-weight: 600; font-size: 32px; line-height: 1.2;
    color: var(--ink); letter-spacing: 1px;
  }
  .benefits { position: absolute; left: 68px; top: 862px; margin: 0; padding: 0; list-style: none; }
  .benefit {
    display: flex; align-items: center; gap: 18px; height: 45px;
    font-weight: 500; font-size: 28px; color: var(--text); letter-spacing: 0.5px;
  }
  .contact {
    position: absolute; left: 58px; top: 1098px; margin: 0; padding: 0; list-style: none;
    font-family: "Lato", sans-serif; font-size: 17px; color: var(--white);
  }
  .contact-item { display: flex; align-items: center; gap: 8px; height: 28px; }
  .phone {
    position: absolute; right: 42px; top: 1138px; margin: 0;
    display: flex; align-items: center; gap: 8px;
    font-family: "Work Sans", sans-serif; font-weight: 600; font-size: 40px; color: var(--white);
  }
</style>
</head>
<body>
<main class="flyer">
  <svg class="flyer-shapes" width="992" height="1200" viewBox="0 0 992 1200" aria-hidden="true">
    <defs>
      <linearGradient id="topBlue" x1="0" y1="0" x2="1" y2="1">
        <stop offset="0" stop-color="#1a4fa8"/>
        <stop offset="1" stop-color="#0a2466"/>
      </linearGradient>
      <linearGradient id="facet" x1="0" y1="0" x2="1" y2="0">
        <stop offset="0" stop-color="#2a6fd1"/>
        <stop offset="1" stop-color="#0b2a6b"/>
      </linearGradient>
      <linearGradient id="bottomBlue" x1="0" y1="0" x2="1" y2="0">
        <stop offset="0" stop-color="#1552b0"/>
        <stop offset="1" stop-color="#0a2466"/>
      </linearGradient>
    </defs>
    <polygon points="0,0 760,0 430,195 778,462 0,424" fill="url(#topBlue)"/>
    <polygon points="0,260 430,195 778,462 0,424" fill="url(#facet)"/>
    <polygon points="0,260 300,300 0,424" fill="#0a2466" opacity="0.55"/>
    <polygon points="0,1002 992,1040 992,1056 0,1018" fill="var(--grey)"/>
    <polygon points="0,1018 992,1056 992,1200 0,1200" fill="url(#bottomBlue)"/>
    <polygon points="600,1200 992,1020 992,1200" fill="#0a2466" opacity="0.6"/>
  </svg>

  <svg class="hero-photo" style="position:absolute;left:0;top:0" width="992" height="700" viewBox="0 0 992 700" role="img" aria-label="Photo of a smiling woman in a red blouse holding a fan of banknotes and giving a thumbs up">
    <defs>
      <linearGradient id="photoTone" x1="0" y1="0" x2="1" y2="1">
        <stop offset="0" stop-color="#e9ebee"/>
        <stop offset="0.6" stop-color="#d6cfca"/>
        <stop offset="1" stop-color="#b8413f"/>
      </linearGradient>
    </defs>
    <polygon points="760,0 992,0 992,650 778,462 430,195" fill="url(#photoTone)"/>
  </svg>

  <p class="brand">HARROWBY LENDING</p>

  <h1 class="headline">HARD MONEY LOANS</h1>
  <p class="rate">RATES FROM 8%</p>

  <section class="services">
    <div class="service" style="left:57px">
      <svg width="170" height="150" viewBox="0 0 170 150" aria-hidden="true">
        <polygon points="45,5 125,5 165,75 125,145 45,145 5,75" fill="none" stroke="var(--navy)" stroke-width="4"/>
        <path d="M52 75 L85 48 L118 75 V108 H52 Z" fill="#333"/>
        <rect x="104" y="50" width="8" height="16" fill="#333"/>
        <path d="M72 92 L98 70 M72 70 L98 92" stroke="var(--white)" stroke-width="5" stroke-linecap="round"/>
      </svg>
      <p class="service-label">FIX &amp; FLIP<br>LOANS</p>
    </div>
    <div class="service" style="left:345px">
      <svg width="170" height="150" viewBox="0 0 170 150" aria-hidden="true">
        <polygon points="45,5 125,5 165,75 125,145 45,145 5,75" fill="none" stroke="var(--navy)" stroke-width="4"/>
        <rect x="54" y="62" width="34" height="50" fill="#333"/>
        <rect x="88" y="40" width="30" height="72" fill="#333"/>
        <g stroke="var(--white)" stroke-width="3">
          <path d="M60 74 H82 M60 84 H82 M60 94 H82 M60 104 H82"/>
          <path d="M96 52 V106 M104 52 V106 M112 52 V106"/>
        </g>
      </svg>
      <p class="service-label">COMMERCIAL<br>LOANS</p>
    </div>
    <div class="service" style="left:649px">
      <svg width="170" height="150" viewBox="0 0 170 150" aria-hidden="true">
        <polygon points="45,5 125,5 165,75 125,145 45,145 5,75" fill="none" stroke="var(--navy)" stroke-width="4"/>
        <circle cx="85" cy="60" r="14" fill="#333"/>
        <text x="85" y="66" text-anchor="middle" font-family="Work Sans, sans-serif" font-weight="600" font-size="17" fill="var(--white)">$</text>
        <circle cx="102" cy="42" r="8" fill="#333"/>
        <path d="M48 92 Q70 84 90 94 L112 88 Q122 86 120 95 L96 110 H60 L48 104 Z" fill="#333"/>
      </svg>
      <p class="service-label">HARD MONEY<br>LOANS</p>
    </div>
  </section>

  <ul class="benefits">
    <li class="benefit">
      <svg width="24" height="24" viewBox="0 0 24 24" aria-hidden="true"><rect x="2" y="3" width="19" height="19" rx="2" fill="none" stroke="var(--ink)" stroke-width="2.5"/><path d="M7 12 L11 16 L22 3" fill="none" stroke="var(--ink)" stroke-width="2.5"/></svg>
      Same-Day Approval
    </li>
    <li class="benefit">
      <svg width="24" height="24" viewBox="0 0 24 24" aria-hidden="true"><rect x="2" y="3" width="19" height="19" rx="2" fill="none" stroke="var(--ink)" stroke-width="2.5"/><path d="M7 12 L11 16 L22 3" fill="none" stroke="var(--ink)" stroke-width="2.5"/></svg>
      No Processing, Appraisal, or Extra Fees
    </li>
    <li class="benefit">
      <svg width="24" height="24" viewBox="0 0 24 24" aria-hidden="true"><rect x="2" y="3" width="19" height="19" rx="2" fill="none" stroke="var(--ink)" stroke-width="2.5"/><path d="M7 12 L11 16 L22 3" fill="none" stroke="var(--ink)" stroke-width="2.5"/></svg>
      100% Financing (w/ Additional Collateral)
    </li>
  </ul>

  <ul class="contact">
    <li class="contact-item">
      <svg width="16" height="16" viewBox="0 0 16 16" aria-hidden="true"><rect x="1" y="1" width="14" height="14" rx="3" fill="var(--white)"/><circle cx="8" cy="8" r="3.5" fill="none" stroke="var(--blue)" stroke-width="1.8"/></svg>
      harrowby802@mail.com
    </li>
    <li class="contact-item">
      <svg width="16" height="16" viewBox="0 0 16 16" aria-hidden="true"><rect x="1" y="1" width="14" height="14" rx="3" fill="var(--white)"/><path d="M3.5 5 H12.5 V11 H3.5 Z M3.5 5 L8 8.5 L12.5 5" fill="none" stroke="var(--blue)" stroke-width="1.3"/></svg>
      http://harrowbylending.com
    </li>
    <li class="contact-item">
      <svg width="16" height="16" viewBox="0 0 16 16" aria-hidden="true"><rect x="1" y="1" width="14" height="14" rx="3" fill="var(--white)"/><path d="M8 13 C5 9.5 4.5 8 4.5 6.5 A3.5 3.5 0 0 1 11.5 6.5 C11.5 8 11 9.5 8 13 Z" fill="var(--blue)"/><circle cx="8" cy="6.5" r="1.3" fill="var(--white)"/></svg>
      1480 Alder Ridge Way, Suite 210 Denver, CO 80211
    </li>
  </ul>

  <p class="phone">
    <svg width="32" height="32" viewBox="0 0 24 24" aria-hidden="true"><path d="M6.6 10.8a15.1 15.1 0 0 0 6.6 6.6l2.2-2.2a1 1 0 0 1 1-.25 11.4 11.4 0 0 0 3.6.57 1 1 0 0 1 1 1V20a1 1 0 0 1-1 1A17 17 0 0 1 3 4a1 1 0 0 1 1-1h3.5a1 1 0 0 1 1 1c0 1.25.2 2.45.57 3.57a1 1 0 0 1-.25 1z" fill="var(--white)"/></svg>
    303.555.0147
  </p>
</main>
</body>
</html>
```